Kelvarine Pools

Luxury pool designer builder brochure

Company name is "Kelvarine"
Tag line is "Pools for the Mind Body & Soul"
Maybe integrate "Luxury Urban Lifestyle"

Target Market(s)

30 to 65 income of 200000.00 plus Affluent, high end life style
Luxury living

Industry/Entity Type

It Company

Font styles to use
Serif

Colors
000000

Requirements
Must have
• NOTE:
• Please remove the "Aquatic environments for the under the logo.
• I want a black background with a very contemporary feel.
• This is a luxury lifestyle product.

```html
<!DOCTYPE html>
<html lang="en">
<head>
<meta charset="utf-8">
<title>Kelvarine Pools – Brochure</title>
<link href="https://fonts.googleapis.com/css2?family=Lato:ital,wght@0,400;0,700;1,700&family=Montserrat:wght@300;400;600&display=swap" rel="stylesheet">
<style>
  :root{
    --page:#eeeeee;
    --black:#060606;
    --panel:#121212;
    --panel-mid:#1b1b1b;
    --teal:#7fd8c4;
    --white:#ffffff;
    --soft:#e9e9e9;
    --silver-dark:#8a8a8a;
    --silver-light:#f4f4f4;
    --ink:#222222;
  }
  *{box-sizing:border-box;margin:0;padding:0}
  html,body{width:1200px;height:900px;overflow:hidden;background:var(--page)}
  .canvas{position:relative;width:1200px;height:900px}
  .brochure{
    position:absolute;left:68px;top:70px;width:1065px;height:760px;
    background:var(--black);overflow:hidden;
    box-shadow:0 4px 18px rgba(0,0,0,.25);
    font-family:'Lato',sans-serif;color:var(--white);
  }
  .panel{position:absolute;top:0;height:760px}
  .panel-inside{left:0;width:360px;background:linear-gradient(180deg,#050505 0%,#0b0b0b 60%,#1a1a1a 100%)}
  .panel-contact{left:360px;width:352px;background:radial-gradient(ellipse at 50% 55%,#262626 0%,#141414 60%,#0a0a0a 100%)}
  .panel-cover{left:712px;width:353px;background:radial-gradient(ellipse at 50% 40%,#202020 0%,#101010 70%,#080808 100%)}
  .photo{position:absolute}
  .photo-villa-dusk{left:0;top:0;width:712px;height:188px;
    background:linear-gradient(90deg,#2c3424 0%,#5c5a3e 30%,#c9b58a 55%,#a98b5c 75%,#d7c7a5 100%)}
  .silver-band{position:absolute;left:0;top:210px;width:712px;height:16px;
    background:linear-gradient(90deg,var(--silver-dark),var(--silver-light) 30%,#b5b5b5 55%,var(--silver-light) 75%,var(--silver-dark))}
  .about-title{position:absolute;left:40px;top:246px;font-size:16px;font-weight:700;color:var(--teal);letter-spacing:.5px}
  .about-copy{position:absolute;left:40px;width:292px;font-size:11.5px;font-weight:700;line-height:16px;letter-spacing:.9px;text-align:justify;color:var(--soft)}
  .about-copy.first{top:274px}
  .about-copy.second{top:428px;width:286px}
  .snapshot{position:absolute;background:var(--white);padding:7px;box-shadow:0 3px 8px rgba(0,0,0,.6)}
  .snapshot .fill{width:100%;height:100%}
  .snapshot.one{left:38px;top:528px;width:178px;height:125px;transform:rotate(-10deg)}
  .snapshot.one .fill{background:linear-gradient(135deg,#6a3a22,#c98a4a 45%,#3b5a7a)}
  .snapshot.two{left:162px;top:548px;width:180px;height:130px;transform:rotate(-5deg)}
  .snapshot.two .fill{background:linear-gradient(160deg,#8a9aa0,#57c4d8 45%,#9fe3ea)}
  .wordmark{position:absolute;font-family:'Montserrat',sans-serif;font-weight:300;color:var(--white);letter-spacing:2px;text-align:center}
  .wordmark.contact{left:360px;width:352px;top:428px;font-size:31px}
  .wordmark.cover{left:712px;width:353px;top:82px;font-size:35px}
  .contact-list{position:absolute;left:398px;top:508px;list-style:none}
  .contact-list li{position:relative;padding-left:40px;font-style:italic;font-weight:700;font-size:16px;letter-spacing:1.3px;color:var(--white);line-height:22px}
  .contact-list li svg{position:absolute;left:0;top:2px}
  .contact-list .address{margin-bottom:12px}
  .contact-list .email{margin-bottom:12px}
  .contact-list .phone{font-size:20px;margin-bottom:10px}
  .photo-villa-pool{left:714px;top:186px;width:351px;height:294px;
    background:linear-gradient(180deg,#4a7fb8 0%,#c7a680 35%,#7a6a58 55%,#2f6fb0 75%,#8ac4e8 100%)}
  .tagline{position:absolute;left:712px;width:353px;text-align:center;font-family:'Lato',sans-serif;color:var(--white)}
  .tagline .line-1{display:block;font-size:36px;letter-spacing:1.5px;line-height:40px;margin-top:498px}
  .tagline .line-2{display:block;font-family:'Montserrat',sans-serif;font-weight:600;font-size:62px;color:var(--teal);line-height:62px;letter-spacing:2px}
  .tagline .line-3{display:block;font-size:29px;letter-spacing:1px;line-height:32px}
  .web-bar{position:absolute;left:714px;top:655px;width:351px;height:40px;
    background:linear-gradient(90deg,var(--silver-dark),var(--silver-light) 35%,var(--silver-light) 65%,#a0a0a0);
    color:var(--ink);font-size:16px;letter-spacing:1.2px;text-align:center;line-height:40px}
</style>
</head>
<body>
<div class="canvas">
  <section class="brochure">
    <div class="panel panel-inside"></div>
    <div class="panel panel-contact"></div>
    <div class="panel panel-cover"></div>

    <div class="photo photo-villa-dusk" role="img" aria-label="Photo of a two-storey Mediterranean villa at dusk with palms and lit windows"></div>
    <div class="silver-band"></div>

    <h2 class="about-title">ABOUT US:</h2>
    <p class="about-copy first">Kelvarine Pools and Outdoors is recognized for their innovation and excellence in swimming pool design and construction, having garnered many awards. As a premium choice Houston pool builder and designer, many of the preeminent homes in the Houston area feature our pools and integrated landscaping and outdoor environments.</p>
    <p class="about-copy second">Kelvarine Pools and Outdoors is recognized for their innovation and excellence in swimming pool design and construction, having garnered many awards.</p>

    <div class="snapshot one"><div class="fill" role="img" aria-label="Photo of a lit outdoor living area beside a pool at night"></div></div>
    <div class="snapshot two"><div class="fill" role="img" aria-label="Photo of a turquoise swimming pool with stone decking"></div></div>

    <div class="wordmark contact">Kelvarine</div>
    <ul class="contact-list">
      <li class="address">
        <svg width="28" height="26" viewBox="0 0 28 26"><path d="M14 2 L27 13 H23 V25 H17 V17 H11 V25 H5 V13 H1 Z" fill="var(--teal)"/></svg>
        4820 Larkspur Bend Drive<br>Coralton, Texas 77590
      </li>
      <li class="email">
        <svg width="26" height="18" viewBox="0 0 26 18"><rect x="1" y="1" width="24" height="16" fill="var(--teal)"/><path d="M1 1 L13 10 L25 1" stroke="#141414" stroke-width="1.6" fill="none"/></svg>
        design@kelvarineinc.com
      </li>
      <li class="phone">
        <svg width="24" height="24" viewBox="0 0 24 24"><path d="M6 2 L10 7 L8 10 C9 13 11 15 14 16 L17 14 L22 18 L19 22 C10 21 3 14 2 5 Z" fill="var(--teal)"/></svg>
        555.014.2290
      </li>
      <li class="web">
        <svg width="26" height="26" viewBox="0 0 26 26" fill="none" stroke="var(--teal)" stroke-width="1.6"><circle cx="13" cy="13" r="11"/><ellipse cx="13" cy="13" rx="5" ry="11"/><path d="M2 13 H24 M4 7 H22 M4 19 H22"/></svg>
        www.kelvarinepools.com
      </li>
    </ul>

    <div class="wordmark cover">Kelvarine</div>
    <div class="photo photo-villa-pool" role="img" aria-label="Photo of a luxury villa at twilight with a glowing blue pool in the foreground"></div>
    <h1 class="tagline">
      <span class="line-1">Pools for the</span>
      <span class="line-2">MIND</span>
      <span class="line-3">Body &amp; Soul</span>
    </h1>
    <div class="web-bar">www.kelvarinepools.com</div>
  </section>
</div>
</body>
</html>
```